Dorian's Lawn Service needs a postcard design

I need a design to attract lawn cutting customers. I am a high school junior, focusing on my city and the neighboring city. I think it would be advantageous to let my potential clients know I am earning money for my college education. They should also know, I will be working side by side with my father, who operated his own lawn service for 20 years, so they can be assured of a quality result for their lawn. I will be using state of the art, commercial equipment.

A few things that are unique to my service are; my mower weighs half of what other commercial mowers do (a softer footprint), my mower does NOT throw clippings into mulch or flower beds, at an additional charge I offer bagging of the clippings and/or dog waste clean-up. I am thinking about a two-sided design. I would also like a cartoon style picture of myself riding my mower. If this is something you can create, I can send you a photo of myself and a photo of my mower. If not, I can get this drawing done separately, then send it to you, I would just need to know what kind of file you would need it in. I am not going to have a business name, I want to introduce myself as Dorian to keep it simple and personal. We can add a coupon to the postcard, offering one free cut with commitment to a full 26 week season. The name of my high school is Marlowe High.

The cartoon picture attached is our logo.

Target Market(s)

Homeowners that use a commercial lawn cutting service, homeowners that need a temporary service while they are on vacation

Industry/Entity Type

School

Colors
3176b5
9bcb3c

Requirements
Must have
• An appeal for people to want to help me earn money for my college education. A clear idea they will be getting top notch service. I definitely want a drawing of myself on my mower. Phone # 612-905-3817
• design must work with parcelvaro.com/routeflyermailing guidelines

```html
<!DOCTYPE html>
<html lang="en">
<head>
<meta charset="utf-8">
<title>Dorian's Lawn Service – Postcard</title>
<link href="https://fonts.googleapis.com/css2?family=Itim&family=Oswald:wght@500;700&family=Anton&family=Lilita+One&family=Source+Sans+3:wght@400;600;700&display=swap" rel="stylesheet">
<style>
  :root {
    --backdrop: #e9e4dc;
    --card-edge: #1d1d1d;
    --grass-dark: #2f6b1c;
    --grass-mid: #4f9a2a;
    --grass-light: #6cb23a;
    --copy-yellow: #eee43a;
    --name-yellow: #f7e22a;
    --offer-red: #8c1a1c;
    --tab-red: #c9202f;
    --panel-green: #7ab342;
    --panel-green-light: #8cc24a;
    --brand-green: #9bcb3c;
    --brand-blue: #00a9d4;
    --frame-red: #9b2335;
    --number-navy: #1b2a4a;
    --rider-dark: #3a3536;
    --rider-grey: #9a9a9c;
    --mower-red: #d9434e;
    --white: #ffffff;
  }
  * { box-sizing: border-box; margin: 0; padding: 0; }
  html, body { width: 880px; height: 1200px; overflow: hidden; }
  body { background: var(--backdrop); position: relative; }

  .card { position: absolute; overflow: hidden; }

  /* ---------- Front ---------- */
  .card--front {
    left: 66px; top: 26px; width: 724px; height: 559px;
    border: 2px solid var(--card-edge);
  }
  .front-photo {
    position: absolute; inset: 0;
    background:
      radial-gradient(ellipse at 30% 40%, var(--grass-light) 0%, transparent 60%),
      linear-gradient(160deg, var(--grass-mid) 0%, var(--grass-dark) 55%, var(--grass-mid) 100%);
  }
  .intro {
    position: absolute; font-family: "Itim", cursive; color: var(--copy-yellow);
    font-size: 25px; line-height: 28.8px;
    text-shadow: 1px 1px 2px rgba(0,0,0,.55);
  }
  .intro span { display: block; text-align: justify; text-align-last: justify; white-space: nowrap; }
  .intro--wide { left: 18px; top: 15px; width: 688px; }
  .intro--narrow { left: 342px; top: 101px; width: 364px; }
  .signature {
    position: absolute; right: 18px; top: 218px;
    font-family: "Lilita One", sans-serif; font-size: 27px; color: var(--name-yellow);
    letter-spacing: 1px; text-shadow: 1px 1px 2px rgba(0,0,0,.5);
  }
  .school {
    position: absolute; right: 20px; top: 252px;
    font-family: "Oswald", sans-serif; font-weight: 700; font-size: 78px; line-height: 1;
    color: rgba(235,240,235,.42); letter-spacing: 1px;
  }
  .offer {
    position: absolute; font-family: "Anton", sans-serif; color: var(--white);
    font-size: 29px; line-height: 1; white-space: nowrap;
    text-shadow: 1px 1px 3px rgba(0,0,0,.6);
  }
  .offer em { font-style: normal; color: var(--offer-red); font-size: 40px; text-shadow: none; }
  .offer--one { left: 272px; top: 334px; }
  .offer--two { right: 18px; top: 386px; }

  .services {
    position: absolute; left: 158px; top: 432px; right: 0; bottom: 0;
    background: linear-gradient(180deg, var(--panel-green-light), var(--panel-green));
  }
  .services-tab {
    position: absolute; right: 16px; top: 0; width: 180px; height: 33px;
    background: var(--tab-red); box-shadow: 0 2px 3px rgba(0,0,0,.35);
    font-family: "Itim", cursive; font-size: 25px; color: var(--name-yellow);
    text-align: center; line-height: 33px;
  }
  .services-list {
    position: absolute; left: 6px; top: 32px; list-style: none;
    font-family: "Source Sans 3", sans-serif; color: var(--white); font-size: 17px;
  }
  .services-list li { height: 27px; display: flex; align-items: center; gap: 3px; white-space: nowrap; }
  .services-list small { font-size: 12.5px; margin-left: 4px; }
  .services-list svg { width: 18px; height: 18px; flex: none; }

  /* ---------- Back ---------- */
  .card--back {
    left: 108px; top: 606px; width: 722px; height: 560px;
    background: var(--white); border: 1px solid var(--card-edge);
  }
  .back-art {
    position: absolute; left: 0; top: 0; width: 348px; height: 461px;
    background: linear-gradient(90deg, var(--brand-green) 0%, var(--brand-green) 18%, var(--brand-blue) 62%, var(--brand-blue) 100%);
  }
  .rider-art {
    position: absolute; left: 20px; top: 18px; width: 312px; height: 440px;
    border-radius: 40px 40px 60px 60px;
    background: linear-gradient(180deg, var(--rider-grey) 0%, var(--rider-dark) 45%, var(--mower-red) 80%, var(--mower-red) 100%);
    opacity: .85;
  }
  .back-banner {
    position: absolute; left: 300px; top: 0; width: 242px; height: 178px;
    background: var(--brand-blue);
  }
  .back-frame {
    position: absolute; left: 228px; top: 30px; width: 310px; height: 144px;
    border: 3px solid var(--frame-red); border-radius: 5px;
  }
  .back-name {
    position: absolute; left: 196px; top: 10px; width: 130px; height: 80px;
    overflow: visible;
  }
  .back-name text {
    font-family: "Itim", cursive; font-size: 22px; fill: var(--white); letter-spacing: 1px;
  }
  .promise {
    position: absolute; left: 228px; top: 42px; width: 310px; text-align: center;
    font-family: "Itim", cursive; font-size: 35px; line-height: 39px; color: var(--frame-red);
  }
  .call {
    position: absolute; left: 244px; top: 134px;
    font-family: "Source Sans 3", sans-serif; font-size: 30px; line-height: 36px; white-space: nowrap;
  }
  .call-label { color: var(--white); font-weight: 600; margin-right: 12px; }
  .call-number { color: var(--number-navy); font-weight: 700; }
</style>
</head>
<body>

<section class="card card--front">
  <div class="front-photo" role="img" aria-label="Close-up photo of green lawn with an arm and hand pointing at the message"></div>

  <p class="intro intro--wide">
    <span>I am a high school junior, focusing on my city and the</span>
    <span>neighboring city. I am earning money for my college</span>
    <span>education. I will be working side by side with my father,</span>
  </p>
  <p class="intro intro--narrow">
    <span>who operated his own lawn</span>
    <span>service for 20 years, I will be</span>
    <span>using state of the art,</span>
    <span>commercial equipment.</span>
  </p>
  <p class="signature">- DORIAN</p>

  <p class="school">MARLOWE HIGH</p>

  <p class="offer offer--one">Offering one <em>FREE CUT</em> with</p>
  <p class="offer offer--two">commitment to a full <em>26 WEEK</em> season</p>

  <div class="services">
    <div class="services-tab">My Services</div>
    <ul class="services-list">
      <li><svg viewBox="0 0 24 24"><path fill="#f7e22a" d="M12 1.5l3.2 6.6 7.3 1-5.3 5.1 1.3 7.2L12 18l-6.5 3.4 1.3-7.2L1.5 9.1l7.3-1z"/></svg>My mower leaves a softer footprint<small>(light weight mower)</small></li>
      <li><svg viewBox="0 0 24 24"><path fill="#f7e22a" d="M12 1.5l3.2 6.6 7.3 1-5.3 5.1 1.3 7.2L12 18l-6.5 3.4 1.3-7.2L1.5 9.1l7.3-1z"/></svg>No clippings thrown into mulch or flower beds</li>
      <li><svg viewBox="0 0 24 24"><path fill="#f7e22a" d="M12 1.5l3.2 6.6 7.3 1-5.3 5.1 1.3 7.2L12 18l-6.5 3.4 1.3-7.2L1.5 9.1l7.3-1z"/></svg>Bagging of the clippings and/or dog waste clean-up<small>(at additional charge)</small></li>
    </ul>
  </div>
</section>

<section class="card card--back">
  <div class="back-art"></div>
  <div class="rider-art" role="img" aria-label="Cartoon illustration of Dorian in a school baseball shirt riding a red commercial mower"></div>
  <div class="back-banner"></div>
  <div class="back-frame"></div>
  <svg class="back-name" viewBox="0 0 130 80" aria-label="Dorian">
    <path id="name-arc" d="M14 72 Q40 8 126 14" fill="none"/>
    <text><textPath href="#name-arc">DORIAN</textPath></text>
  </svg>
  <p class="promise">We Assured<br>Quality Results</p>
  <p class="call"><span class="call-label">CALL:</span><span class="call-number">612-905-3817</span></p>
</section>

</body>
</html>
```